Brightvale HQ letterhead and envelope

Design a formal (8.5x11) letterhead and envelope for sales outreach and legal matters. Using design input from https://www.brightvalehq.example/ and the attached documents.

Industry/Entity Type

Software Service

Requirements
Must have
• These 4 hex colors are our official colors:
• #355c98 [blue]
• #1eb1a2 [teal]
• #fdba12 [gold]
• #f1653b [orange]
• So no other colors besides these should be used.

```html
<!DOCTYPE html>
<html lang="en">
<head>
<meta charset="utf-8">
<title>Brightvale HQ — Letterhead and Envelope</title>
<link href="https://fonts.googleapis.com/css2?family=Roboto:wght@300;400;500&display=swap" rel="stylesheet">
<style>
  :root {
    --blue: #355c98;
    --teal: #1eb1a2;
    --gold: #fdba12;
    --orange: #f1653b;
    --paper: #f4f4f4;
    --ink: #6f6f6f;
    --ink-dark: #3c3c3c;
    --backdrop: #d6d6d6;
  }
  * { box-sizing: border-box; margin: 0; padding: 0; }
  html, body { width: 1200px; height: 810px; overflow: hidden; }
  body {
    position: relative;
    background: var(--backdrop);
    font-family: "Roboto", Arial, sans-serif;
    color: var(--ink);
  }
  .sheet {
    position: absolute;
    background: var(--paper);
    box-shadow: 0 8px 22px rgba(0,0,0,0.22);
    overflow: hidden;
  }
  .brand { display: flex; align-items: center; gap: 8px; color: var(--blue); font-weight: 300; }
  .brand-dot { border: 2.5px solid var(--blue); border-radius: 50%; flex: none; }
  .brand-name { white-space: nowrap; letter-spacing: 0.2px; }
  .color-band { position: absolute; left: 0; bottom: 0; width: 100%; }

  /* Letterhead */
  .letterhead { left: 137px; top: 110px; width: 436px; height: 614px; }
  .letterhead .brand { position: absolute; left: 27px; top: 48px; }
  .letterhead .brand-dot { width: 32px; height: 32px; }
  .letterhead .brand-name { font-size: 23px; }
  .contact-direct, .contact-office {
    position: absolute; top: 51px; font-size: 7.4px; line-height: 10px;
  }
  .contact-direct { left: 238px; color: var(--ink-dark); font-weight: 500; }
  .contact-office { left: 340px; color: var(--ink); }
  .contact-divider { position: absolute; left: 330px; top: 52px; width: 1px; height: 28px; background: #b5b5b5; }
  .recipient { position: absolute; left: 39px; top: 190px; font-size: 7.6px; line-height: 11.5px; }
  .letter-body { position: absolute; left: 39px; top: 258px; width: 363px; font-size: 7.4px; line-height: 11.4px; text-align: justify; }
  .letter-body p + p { margin-top: 11px; }
  .signature {
    position: absolute; left: 39px; top: 428px; width: 82px; height: 46px;
    background: linear-gradient(135deg, #e8e8e8, #dcdcdc); border-radius: 4px;
  }
  .sign-title { position: absolute; left: 39px; top: 493px; font-size: 7.6px; }
  .letterhead .color-band { height: 10px; }

  /* Envelope back */
  .envelope-back { left: 619px; top: 192px; width: 444px; height: 223px; }
  .envelope-back svg { position: absolute; left: 0; top: 0; }

  /* Envelope front */
  .envelope-front { left: 618px; top: 444px; width: 445px; height: 220px; }
  .envelope-front .brand { position: absolute; left: 22px; top: 21px; gap: 7px; }
  .envelope-front .brand-dot { width: 24px; height: 24px; border-width: 2px; }
  .envelope-front .brand-name { font-size: 17.5px; }
  .envelope-front .contact-direct { left: 25px; top: 69px; }
  .envelope-front .contact-office { left: 25px; top: 104px; }
  .envelope-front .color-band { height: 9px; }
</style>
</head>
<body>

<section class="sheet letterhead" aria-label="Letterhead">
  <div class="brand"><span class="brand-dot"></span><span class="brand-name">Brightvale HQ</span></div>
  <div class="contact-direct">(555) 010-2040<br>jsmith@brightvalehq.example<br>www.brightvalehq.example</div>
  <div class="contact-divider"></div>
  <div class="contact-office">Main: (555) 013-7788<br>214 Orchard Lane<br>Fairview, MI 40010</div>

  <div class="recipient">Dear Mr. Harlow<br>Northfield Print Group<br>Department Design</div>

  <div class="letter-body">
    <p>Lorem ipsum dolor sit amet, consectetuer adipiscing elit. Aenean commodo ligula eget dolor. Aenean massa. Cum sociis natoque penatibus et magnis dis parturient montes, nascetur ridiculus mus. Donec quam felis, ultricies nec, pellentesque eu, pretium quis, sem. Nulla consequat massa quis enim. Donec pede justo, fringilla vel, aliquet nec, vulputate eget, arcu. In enim justo, rhoncus ut, imperdiet a, venenatis vitae, justo. Nullam dictum felis eu pede mollis pretium. Integer tincidunt. Cras dapibus. Vivamus elementum semper nisi.Nullam dictum felis eu pede mollis pretium. Integer tincidunt. Cras dapibus. Vivamus elementum semper nisi.felis eu pede mollis pretium. Integer tincidunt. Cras dapibus.</p>
    <p>Quisque rutrum. Aenean imperdiet. Etiam ultricies nisi vel augue. Curabitur ullamcorper ultricies nisi. Nam eget dui. Etiam rhoncus. Maecenas tempus, tellus eget condimentum rhoncus, sem quam semper libero, sit amet adipiscing sem neque sed ipsum.felis pede mollis pretium. I am tincidunt. Cras dapibus.</p>
  </div>

  <div class="signature" role="img" aria-label="Handwritten signature"></div>
  <div class="sign-title">Director/Excecutive Director</div>

  <svg class="color-band" viewBox="0 0 436 10" preserveAspectRatio="none" aria-hidden="true">
    <polygon points="0,0 263,0 270,10 0,10" fill="var(--blue)"/>
    <polygon points="266,0 436,0 436,10 273,10" fill="var(--gold)"/>
  </svg>
</section>

<section class="sheet envelope-back" aria-label="Envelope back">
  <svg width="444" height="70" viewBox="0 0 444 70" aria-hidden="false">
    <defs>
      <linearGradient id="flapTone" x1="0" y1="0" x2="1" y2="0">
        <stop offset="0" stop-color="#f1ece8"/>
        <stop offset="0.5" stop-color="#eef0f1"/>
        <stop offset="1" stop-color="#f2ede6"/>
      </linearGradient>
    </defs>
    <path d="M0,0 H444 L434,58 Q432,66 424,66 H20 Q12,66 10,58 Z" fill="rgba(0,0,0,0.08)" transform="translate(0,2)"/>
    <path role="img" aria-label="Pattern of small scattered icons in brand colours on the flap"
          d="M0,0 H444 L434,58 Q432,64 424,64 H20 Q12,64 10,58 Z" fill="url(#flapTone)"/>
  </svg>
</section>

<section class="sheet envelope-front" aria-label="Envelope front">
  <div class="brand"><span class="brand-dot"></span><span class="brand-name">Brightvale HQ</span></div>
  <div class="contact-direct">(555) 010-2040<br>jsmith@brightvalehq.example<br>brightvalehq.example</div>
  <div class="contact-office">Main: (555) 013-7788<br>214 Orchard Lane<br>Fairview, MI 40010</div>
  <svg class="color-band" viewBox="0 0 445 9" preserveAspectRatio="none" aria-hidden="true">
    <polygon points="0,0 267,0 274,9 0,9" fill="var(--blue)"/>
    <polygon points="270,0 445,0 445,9 277,9" fill="var(--gold)"/>
  </svg>
</section>

</body>
</html>
```